Full color cover for Chamber's Membership Menu

I need a cover, 8 1/2" x 11" for our Chamber of Commerce Membership Menu. Is should have our logo and the words, Membership Menu on it. That's all that is necessary but it can include one or more of the other photos (maybe a college?) that I added, though they are not required. Our logo colors should be used: 37-170-226, 58-181-74, 40-56-144, 247-148-29, 189-190-192.

Target Market(s)

Business owners and managers

Industry/Entity Type

Business Development

Font styles to use
Serif

Colors
0054AA
0677BA
7BADD7
CADEEF
E8F1F8
00AB8E
00BBA5
67D7C9
C6EFE9
E9F9F6
F0912C
F2A743
F7CA91
FBE8D2
FDF5EE

Requirements
Must have
• Our logo and the words Membership Menu
Nice to have
• An attractive business-like feel. It can be very simple.

```html
<!DOCTYPE html>
<html lang="en">
<head>
<meta charset="utf-8">
<title>Membership Menu Cover</title>
<link rel="stylesheet" href="https://fonts.googleapis.com/css2?family=Cinzel:wght@500&family=Roboto:wght@500&display=swap">
<style>
  :root {
    --brand-navy: #283890;
    --brand-blue: #0054AA;
    --brand-sky: #25AAE2;
    --brand-green: #3AB54A;
    --brand-orange: #F7941D;
    --brand-grey: #BDBEC0;
    --paper: #F4F5F6;
    --photo-dark: #2E2A2C;
    --photo-warm: #8C6A5A;
  }
  html, body {
    margin: 0;
    padding: 0;
    overflow: hidden;
  }
  body {
    width: 845px;
    height: 1200px;
    background: #FFFFFF;
  }
  .cover {
    position: relative;
    width: 845px;
    height: 1200px;
    background: radial-gradient(ellipse at 50% 45%, #FFFFFF 0%, var(--paper) 75%);
    overflow: hidden;
  }
  .cover__waves {
    position: absolute;
    inset: 0;
  }
  .identity {
    position: absolute;
    top: 150px;
    left: 0;
    width: 100%;
    text-align: center;
    color: var(--brand-navy);
    font-family: "Roboto", Arial, sans-serif;
    font-weight: 500;
  }
  .identity__mark {
    width: 62px;
    height: 62px;
    margin: 0 auto 26px;
    border-radius: 50%;
    background: var(--brand-navy);
  }
  .identity__name {
    margin: 0;
    font-size: 31px;
    line-height: 1;
    letter-spacing: -0.3px;
  }
  .identity__tagline {
    margin: 4px 0 0;
    font-size: 16px;
    line-height: 1;
    letter-spacing: 4.6px;
  }
  .collage {
    position: absolute;
    left: 0;
    top: 0;
  }
  .title {
    position: absolute;
    top: 966px;
    left: 168px;
    width: 507px;
    height: 80px;
    border-top: 1px solid var(--brand-navy);
    border-bottom: 1px solid var(--brand-navy);
    box-sizing: border-box;
    display: flex;
    align-items: center;
    justify-content: center;
    margin: 0;
    font-family: "Cinzel", "Times New Roman", serif;
    font-weight: 500;
    font-size: 45px;
    letter-spacing: 1px;
    color: var(--brand-navy);
  }
</style>
</head>
<body>
  <main class="cover">
    <svg class="cover__waves" width="845" height="1200" viewBox="0 0 845 1200" aria-hidden="true">
      <path class="wave wave--top" fill="var(--brand-blue)"
        d="M0 0 H845 V58 C700 30 560 40 420 78 C280 112 120 108 0 60 Z"/>
      <path class="wave-line wave-line--top" fill="none" stroke="var(--brand-grey)" stroke-width="4"
        d="M0 70 C120 118 280 124 420 88 C560 52 700 40 845 66"/>
      <path class="wave-line wave-line--bottom" fill="none" stroke="var(--brand-grey)" stroke-width="4"
        d="M0 1126 C160 1110 320 1092 480 1068 C620 1046 740 1040 845 1088"/>
      <path class="wave wave--bottom" fill="var(--brand-orange)"
        d="M0 1138 C160 1124 320 1106 480 1082 C620 1062 740 1058 845 1102 V1200 H0 Z"/>
    </svg>

    <header class="identity">
      <div class="identity__mark"></div>
      <p class="identity__name">HARBORVIEW CHAMBER</p>
      <p class="identity__tagline">OF COMMERCE &amp; TOURISM</p>
    </header>

    <svg class="collage" width="845" height="1200" viewBox="0 0 845 1200" role="img"
      aria-label="Collage of photographs from chamber events: members at networking mixers, a ribbon cutting and staff in aprons, set inside the county outline">
      <defs>
        <linearGradient id="collage-tone" x1="0" y1="0" x2="1" y2="1">
          <stop offset="0" stop-color="var(--photo-warm)"/>
          <stop offset="0.55" stop-color="var(--photo-dark)"/>
          <stop offset="1" stop-color="#5A4A48"/>
        </linearGradient>
      </defs>
      <rect x="130" y="400" width="585" height="520" rx="40" fill="url(#collage-tone)"
        stroke="var(--brand-navy)" stroke-width="5"/>
    </svg>

    <h1 class="title">MEMBERSHIP MENU</h1>
  </main>
</body>
</html>
```